依頼詳細
両面フルカラーでお願いします。

【表】
SEOやコンサルタントといった自分の知識を商材としますので、誠実さが伝わるデザインを希望します。ただ、誠実すぎて硬すぎるデザインではなくスタイリッシュなデザインになるようにしてください。

【裏】
将来の展望として大学生など若い世代や企業といった様々な人との関わりを持ちたいと考えております。幅広い世代にウケる遊び心のあるデザインをお願いします。

【ロゴについて】
ロゴのデザインは人と企業と弊社がつながっているロゴになっています。
名刺でも人のつながりと拡散が伝わるようなデザインになれればお願いします。
記載項目
表面:会社名/役職/名前/住所/電話/FAX/携帯番号/Mail/URL
裏面:社名(ロゴ可)/名前
希望イメージ
シンプル 複雑
単色 カラフル
暗い 明るい
日常 高級
遊び心 厳粛
未来的 伝統的
女性的 男性的
希望する色
お任せします。
納品ファイル
• イラストレーター形式 (.ai)
• フォトショップ形式 (.psd)
• PNG形式 (.png)
補足説明
自社サービスなどができてくると、背面デザインを変える事になると思います。そうなった時には都度お仕事を依頼できればと思います。
大変失礼いたしました。
会社名が抜けておりました。

登記する会社名は「株式会社ブライトピーク」となります。
ただ、株式会社にするか合同にするかまだ本決定していないので後で変更をお願いするかもしれません。

提案書などのコピーライトで使う会社名は「BRIGHTPEAK」となります。
デザイン表現のなかで英語表記がしっくりくるようでしたら英語表記でも問題ありません。
ロゴ画像が添付できていなかったようですので添付いたします。
失礼いたしました。
ロゴaiデータのバージョンを落としました。
CS2に落とすことと、PDF変換を付けましたので、現在掲載しているロゴデータが開けられない方はこちらをご利用ください。

変換ファイル

よろしくお願いいたします。
選定確約を付けさせていただきました。

また、ロゴの提供が遅れてしまったことや土日をまたいで、より多くのご提案を言頂きたいと思いましたので、期間を延長させていただきました。

まだまだ、ご提案をお待ちしておりますので、
ご提案いただいた方も、今やられている方も、引き続きよろしくお願いいたします。
■ 選んだ理由

表面の配置がとても綺麗でまとまりがありましたので、こちらのデザインとさせていただきました。

■ 提案者全員のお礼・コメント

多くのご提案本当にありがとうございました。どれも良いデザインで全て使わせていただきたいくらいだったのですが、社員に聞いてみて全体で決めさせていただきました。選ばれなかった方も選ばれた方もとてもユニークなアイデアを下さりありがとうございました。

```html
<!DOCTYPE html>
<html lang="ja">
<head>
<meta charset="utf-8">
<title>BRIGHT PEAK 名刺</title>
<link rel="stylesheet" href="https://fonts.googleapis.com/css2?family=Montserrat:wght@700&family=Noto+Sans+JP:wght@400;700&display=swap">
<style>
  :root {
    --brand-blue: #203f97;
    --brand-yellow: #f4b400;
    --pale-yellow: #fbeecb;
    --ink: #333333;
    --muted: #555555;
    --paper: #ffffff;
    --backdrop: #ffffff;
    --shadow: rgba(0, 0, 0, 0.28);
  }
  * { margin: 0; padding: 0; box-sizing: border-box; }
  html, body {
    width: 900px; height: 1200px; overflow: hidden;
    background: var(--backdrop);
    font-family: "Noto Sans JP", sans-serif;
    color: var(--ink);
  }
  .card {
    position: absolute;
    left: 60px; width: 786px; height: 480px;
    background: var(--paper);
    box-shadow: 2px 4px 10px var(--shadow);
    overflow: hidden;
  }
  .card--front { top: 60px; }
  .card--back { top: 680px; }

  .wordmark {
    display: flex; align-items: center; gap: 14px;
    font-family: "Montserrat", sans-serif; font-weight: 700;
    color: var(--brand-blue); letter-spacing: 1px;
  }
  .wordmark__dot {
    border-radius: 50%; background: var(--brand-yellow); flex: none;
  }

  /* front */
  .front__wordmark { position: absolute; left: 42px; top: 150px; font-size: 40px; }
  .front__wordmark .wordmark__dot { width: 34px; height: 34px; }
  .front__company {
    position: absolute; left: 42px; top: 238px;
    font-size: 16px; font-weight: 700; color: var(--brand-blue);
  }
  .front__address {
    position: absolute; left: 42px; top: 268px;
    font-size: 13px; line-height: 24px; color: var(--muted);
  }
  .front__person { position: absolute; left: 432px; top: 150px; }
  .front__title { font-size: 15px; }
  .front__name-row { display: flex; align-items: baseline; gap: 12px; margin-top: 8px; }
  .front__name { font-size: 30px; letter-spacing: 6px; }
  .front__romaji { font-size: 13px; color: var(--muted); }
  .front__mobile { font-size: 14px; margin-top: 10px; }
  .front__backdrop-name {
    position: absolute; left: 30px; top: 378px;
    font-family: "Montserrat", sans-serif; font-weight: 700;
    font-size: 92px; letter-spacing: 10px; white-space: nowrap;
    color: var(--pale-yellow);
  }

  /* back */
  .corner-arcs { position: absolute; inset: 0; }
  .back__brand {
    position: absolute; left: 0; right: 0; top: 130px;
    display: flex; flex-direction: column; align-items: center;
  }
  .back__wordmark { font-size: 42px; }
  .back__wordmark .wordmark__dot { width: 36px; height: 36px; }
  .back__company { font-size: 17px; font-weight: 700; margin-top: 34px; }
  .back__name {
    font-size: 38px; font-weight: 700; letter-spacing: 14px;
    color: var(--brand-blue); margin-top: 34px; padding-left: 14px;
  }
  .back__name-accent { color: var(--brand-yellow); }
  .back__romaji { font-size: 13px; color: var(--brand-blue); margin-top: 4px; }
</style>
</head>
<body>

<section class="card card--front">
  <div class="front__backdrop-name" aria-hidden="true">BRIGHT PEAK</div>
  <div class="wordmark front__wordmark"><span class="wordmark__dot"></span>BRIGHT PEAK</div>
  <p class="front__company">株式会社ブライトピーク</p>
  <p class="front__address">
    〒150-0001 東京都渋谷区神宮前1-2-3<br>
    TEL/ 03-1234-5678　FAX/ 03-1234-5679<br>
    E-mail/ info@brightpeak.example　https://brightpeak.example
  </p>
  <div class="front__person">
    <p class="front__title">代表取締役</p>
    <div class="front__name-row">
      <span class="front__name">山田一郎</span>
      <span class="front__romaji">Yamada Ichiro</span>
    </div>
    <p class="front__mobile">携帯　080-1234-5678</p>
  </div>
</section>

<section class="card card--back">
  <svg class="corner-arcs" width="786" height="480" viewBox="0 0 786 480" aria-hidden="true">
    <g fill="none" stroke-width="22">
      <circle cx="786" cy="0" r="52" stroke="var(--brand-yellow)"/>
      <circle cx="0" cy="480" r="52" stroke="var(--brand-blue)"/>
      <circle cx="786" cy="480" r="52" stroke="var(--brand-blue)"/>
    </g>
  </svg>
  <div class="back__brand">
    <div class="wordmark back__wordmark"><span class="wordmark__dot"></span>BRIGHT PEAK</div>
    <p class="back__company">株式会社ブライトピーク</p>
    <p class="back__name">山<span class="back__name-accent">田</span>一郎</p>
    <p class="back__romaji">Yamada Ichiro</p>
  </div>
</section>

</body>
</html>
```